Professional and Modern Company Letterhead for Fintech Startup

Brisk lending is a fintech startup that provides home financing.

Our company requires letterhead in Microsoft word format. Colors must come from our ADA compliant doc.

Company logo, equal housing opportunity logo, and legal language must be included somewhere on the document.

We'd love an option that maximizes space on the page for text vs have design take up the entire thing.

Target Market(s)

Partners, clients, and employees

Industry/Entity Type

Finance

Font styles to use
Sans Serif

Requirements
Must have
• Must use company colors that are ADA compliant (see attachment). Must include logo in a prominent position. Must include equal housing opportunity logo and legal info at the bottom:

©Brisk Lending LLC. NMLS #5093374 | 4716 Harlow Avenue #204, Boulder, CO 80305 | Not available in all states | 800.437.5068 | help@brisklending-example.com
Nice to have
• Something modern and clean.

```html
<!DOCTYPE html>
<html lang="en">
<head>
<meta charset="utf-8">
<title>Brisk lending – Letterhead</title>
<link href="https://fonts.googleapis.com/css2?family=Questrial&display=swap" rel="stylesheet">
<style>
  :root {
    --backdrop: #808080;
    --paper: #f6f3f3;
    --brand-teal: #31b8c7;
    --ink: #4a4a4a;
    --ink-soft: #555555;
    --on-brand: #ffffff;
  }
  * { box-sizing: border-box; margin: 0; padding: 0; }
  html, body {
    width: 1072px; height: 1200px; overflow: hidden;
    background: var(--backdrop);
    font-family: "Questrial", "Century Gothic", sans-serif;
    color: var(--ink);
  }
  .letterhead {
    position: absolute; left: 199px; top: 132px;
    width: 682px; height: 962px;
    background: var(--paper);
  }
  .brand {
    position: absolute; left: 68px; top: 66px;
    display: flex; align-items: center; gap: 8px;
  }
  .brand-mark {
    width: 14px; height: 14px; background: var(--brand-teal);
  }
  .brand-name {
    font-size: 30px; color: var(--brand-teal); letter-spacing: -0.3px;
  }
  .contact {
    position: absolute; left: 490px; top: 73px;
    font-size: 11.5px; line-height: 14.4px; color: var(--ink-soft);
  }
  .contact-address { margin-bottom: 5px; }
  .contact-line { display: flex; align-items: center; gap: 7px; margin-left: -16px; }
  .contact-line svg { width: 9px; height: 9px; flex: none; }
  .letter {
    position: absolute; left: 68px; top: 268px; width: 550px;
  }
  .salutation {
    font-size: 20px; font-weight: 400; color: var(--ink-soft); margin-bottom: 30px;
  }
  .letter-body p {
    font-size: 11.5px; line-height: 16.4px; text-align: justify;
    margin-bottom: 16.4px; hyphens: auto;
  }
  .closing { font-size: 11.5px; margin-top: 26px; }
  .signature {
    display: block; width: 88px; height: 36px; margin-top: 8px;
    background: linear-gradient(90deg, rgba(40,48,64,0.18), rgba(40,48,64,0.06));
  }
  .legal-band {
    position: absolute; left: 0; top: 906px; width: 682px; height: 28px;
    background: var(--brand-teal); color: var(--on-brand);
    font-size: 11.5px; display: flex; align-items: center; justify-content: center;
  }
</style>
</head>
<body>
  <main class="letterhead">
    <header>
      <div class="brand">
        <span class="brand-mark"></span>
        <span class="brand-name">Brisk lending</span>
      </div>
      <address class="contact" style="font-style:normal">
        <div class="contact-address">4716 Harlow Avenue #204<br>Boulder, CO 80305</div>
        <div class="contact-line">
          <svg viewBox="0 0 10 10" aria-hidden="true"><path d="M2 0.5 L3.8 2.6 L2.9 3.8 C3.6 5.3 4.7 6.4 6.2 7.1 L7.4 6.2 L9.5 8 L8.4 9.5 C4.4 9.2 0.8 5.6 0.5 1.6 Z" fill="var(--brand-teal)"/></svg>
          <span>800.437.5068</span>
        </div>
        <div class="contact-line">
          <svg viewBox="0 0 10 10" aria-hidden="true"><rect x="0.5" y="2" width="9" height="6.5" fill="var(--brand-teal)"/><path d="M0.8 2.3 L5 5.6 L9.2 2.3" stroke="var(--paper)" stroke-width="0.9" fill="none"/></svg>
          <span>help@brisklending-example.com</span>
        </div>
      </address>
    </header>

    <section class="letter">
      <h1 class="salutation">Dear Mr. Carver,</h1>
      <div class="letter-body">
        <p>Lorem ipsum dolor sit amet, consectetur adipiscing elit. Donec orci purus, luctus vitae dignissim eu, iaculis sed purus. Vivamus faucibus, ipsum nec aliquet viverra, leo mauris condimentum ligula, sit amet sagittis enim ligula quis arcu. Nam egestas tortor id nisi porttitor mattis. In tortor ante, ultricies in suscipit a, tempus non massa. Vivamus et auctor mi. Fusce vel massa nulla. Phasellus nec eros mauris, et scelerisque orci.</p>
        <p>Donec malesuada orci vitae nulla accumsan porta a id massa. Quisque accumsan iaculis magna sit amet fringilla. Maecenas consequat, magna eget tincidunt semper, odio nibh rutrum mi, id feugiat ante nisi eu risus. Vestibulum nunc orci, rhoncus a placerat in, ultricies in mi. Cras mattis varius eros, vel fringilla nisi suscipit eget. Quisque scelerisque sagittis nulla at porttitor.</p>
        <p>Sed id augue vitae urna euismod commodo aliquet a quam. Pellentesque arcu velit, cursus et malesuada ut, consequat et diam. Nullam erat sem, rhoncus id ullamcorper vitae, rhoncus et arcu. In ultricies ultricies nulla, ut rutrum nisi iaculis at. Donec eu magna a metus ornare faucibus. Fusce aliquet faucibus ultricies. Morbi semper, est id tincidunt gravida, sem arcu adipiscing lacus, ac bibendum nulla leo eu purus. Quisque nec diam sed risus consectetur a ccumsan quis quis nibh. Vestibulum id purus lorem.</p>
        <p>It is a long established fact that a reader will be distracted by the readable content of a page when looking at its layout. The point of using Lorem Ipsum is that it has a more-or-less normal distribution of letters, as opposed to using 'Content here, content here', making it look like readable English. Many desktop publishing packages</p>
      </div>
      <p class="closing">Sincerely,</p>
      <span class="signature" role="img" aria-label="Handwritten signature of the sender"></span>
    </section>

    <footer class="legal-band">©Brisk Lending LLC. &nbsp;|&nbsp;NMLS #5093374&nbsp;|&nbsp;Not available in all states</footer>
  </main>
</body>
</html>
```